Design layout of business card

Create a business card using existing logo and company information.
Our newly established business provides advice to family owned businesses for their succession planning, value improvement and also on business sales and acquisitions.

Target Market(s)

Owners of family businesses

Contact Information for Business Card

Key contact details are:
Grant Mellowby
Director
P: 08 9482 3157
W: 0431 587 219
Address: Unit 4, 35 Talbrook Lane, Dunsborough, WA, 6281
Website: kinholdadvisory.com.au
Email: grant@kinholdadvisory.com.au

In smaller font somewhere needs to be these details:
ABN: 47 291 803 556
Licensed Real Estate & Business Agent No. RA53917
KTR Adviser Holdings Pty Ltd
AFSL No. 529361

Font styles to use
Sans Serif

Requirements
Must have
• Kinhold Advisory Group logo to feature on front.
• Remaining logos to be included smaller and on back.
• Oakvale Trade Brokers logo to have words 'Powered by' next to it and to be the first of the uploaded logo files.
• Colours on card should complement the logo
Nice to have
• Clear and clean layout
• Logos for contact details for conciseness e.g. phone icon for mobile

```html
<!DOCTYPE html>
<html lang="en">
<head>
<meta charset="utf-8">
<title>Kinhold Advisory Group – Business Card</title>
<link rel="stylesheet" href="https://fonts.googleapis.com/css2?family=Signika:wght@300;400;600&display=swap">
<style>
  :root {
    --stage: #bcbdc0;
    --card: #ffffff;
    --brand-orange: #f15a29;
    --brand-grey: #9a9ea3;
    --ink: #1e1e1e;
    --navy: #1f3a68;
    --slate: #3a3d46;
  }
  * { margin: 0; padding: 0; box-sizing: border-box; }
  html, body { width: 1022px; height: 1200px; overflow: hidden; }
  body {
    background: var(--stage);
    font-family: "Signika", "Helvetica Neue", Arial, sans-serif;
    color: var(--ink);
    position: relative;
  }
  .card {
    position: absolute;
    left: 23px;
    width: 976px;
    height: 557px;
    background: var(--card);
  }
  .card--front { top: 23px; }
  .card--back { top: 620px; }

  /* Front */
  .brand {
    position: absolute;
    left: 40px;
    top: 78px;
    display: flex;
    align-items: center;
    gap: 16px;
  }
  .brand__mark {
    width: 56px; height: 56px;
    border-radius: 50%;
    background: var(--brand-grey);
    flex: none;
  }
  .brand__name {
    font-weight: 600;
    font-size: 32px;
    line-height: 1;
    color: var(--slate);
    white-space: nowrap;
  }
  .contact-person {
    position: absolute;
    left: 719px;
    top: 82px;
    width: 257px;
  }
  .contact-person__rule {
    height: 11px;
    background: var(--brand-orange);
    margin-bottom: 6px;
  }
  .contact-person__name {
    font-weight: 600;
    font-size: 31px;
    line-height: 35px;
    color: var(--brand-grey);
  }
  .contact-person__role {
    font-weight: 300;
    font-size: 30px;
    line-height: 35px;
  }
  .contacts {
    position: absolute;
    left: 203px;
    top: 326px;
    list-style: none;
  }
  .contacts__item {
    display: flex;
    align-items: center;
    gap: 13px;
    height: 38px;
    font-weight: 300;
    font-size: 29px;
    white-space: nowrap;
  }
  .contacts__icon { width: 26px; height: 26px; flex: none; }

  /* Back */
  .affiliation {
    position: absolute;
    left: 200px;
    top: 63px;
    display: flex;
    align-items: center;
    gap: 12px;
  }
  .affiliation__mark {
    width: 56px; height: 56px;
    border-radius: 50%;
    background: var(--navy);
    flex: none;
  }
  .affiliation__name {
    font-weight: 600;
    font-size: 21px;
    color: var(--navy);
  }
  .badge {
    position: absolute;
    left: 200px;
    top: 154px;
    width: 75px; height: 75px;
    border-radius: 50%;
    border: 3px solid var(--navy);
  }
  .powered {
    position: absolute;
    left: 201px;
    top: 383px;
  }
  .powered__label {
    font-weight: 300;
    font-size: 23px;
    color: var(--slate);
    margin-bottom: 10px;
  }
  .powered__brand {
    display: flex;
    align-items: center;
    gap: 10px;
    font-weight: 600;
    font-size: 21px;
    color: var(--slate);
  }
  .powered__square { width: 22px; height: 22px; background: var(--slate); flex: none; }
  .legal {
    position: absolute;
    left: 618px;
    top: 386px;
    font-weight: 300;
    font-size: 23px;
    line-height: 28px;
    white-space: nowrap;
  }
</style>
</head>
<body>

<section class="card card--front" aria-label="Card front">
  <div class="brand">
    <span class="brand__mark" aria-hidden="true"></span>
    <span class="brand__name">Kinhold Advisory Group</span>
  </div>

  <div class="contact-person">
    <div class="contact-person__rule"></div>
    <div class="contact-person__name">Grant Mellowby</div>
    <div class="contact-person__role">Director</div>
  </div>

  <ul class="contacts">
    <li class="contacts__item">
      <svg class="contacts__icon" viewBox="0 0 28 28" aria-hidden="true"><circle cx="14" cy="14" r="14" fill="var(--brand-orange)"/><path d="M9 8.5c1-1 2-1 2.5 0l1.2 2.2c.3.6 0 1.2-.5 1.6l-.6.5c.8 1.7 2 2.9 3.6 3.6l.5-.6c.4-.5 1-.8 1.6-.5l2.2 1.2c1 .5 1 1.5 0 2.5-1.2 1.2-3 1.3-5.2 0-2.3-1.4-4.2-3.3-5.5-5.6-1.2-2-1.1-3.700.2-4.9z" fill="none" stroke="#fff" stroke-width="1.3"/></svg>
      <span>08 9482 3157</span>
    </li>
    <li class="contacts__item">
      <svg class="contacts__icon" viewBox="0 0 28 28" aria-hidden="true"><circle cx="14" cy="14" r="14" fill="var(--brand-orange)"/><path d="M14 21.5s-5-5.3-5-9a5 5 0 0 1 10 0c0 3.7-5 9-5 9z" fill="none" stroke="#fff" stroke-width="1.4"/><circle cx="14" cy="12.5" r="1.8" fill="none" stroke="#fff" stroke-width="1.3"/></svg>
      <span>0431 587 219</span>
    </li>
    <li class="contacts__item">
      <svg class="contacts__icon" viewBox="0 0 28 28" aria-hidden="true"><circle cx="14" cy="14" r="14" fill="var(--brand-orange)"/><path d="M7.5 14L14 8l6.5 6M9.5 12.5V20h9v-7.5M12.5 20v-4h3v4" fill="none" stroke="#fff" stroke-width="1.4" stroke-linejoin="round"/></svg>
      <span>Unit 4, 35 Talbrook Lane, Dunsborough, WA, 6281</span>
    </li>
    <li class="contacts__item">
      <svg class="contacts__icon" viewBox="0 0 28 28" aria-hidden="true"><circle cx="14" cy="14" r="14" fill="var(--brand-orange)"/><g fill="none" stroke="#fff" stroke-width="1.2"><circle cx="14" cy="14" r="6.5"/><ellipse cx="14" cy="14" rx="2.8" ry="6.5"/><path d="M7.5 14h13M8.5 10.8h11M8.5 17.2h11"/></g></svg>
      <span>kinholdadvisory.com.au</span>
    </li>
    <li class="contacts__item">
      <svg class="contacts__icon" viewBox="0 0 28 28" aria-hidden="true"><circle cx="14" cy="14" r="14" fill="var(--brand-orange)"/><g fill="none" stroke="#fff" stroke-width="1.3" stroke-linejoin="round"><rect x="7.5" y="9.5" width="13" height="9"/><path d="M7.5 9.5l6.5 5.5 6.5-5.5M7.5 18.5l4.5-4M20.5 18.5l-4.5-4"/></g></svg>
      <span>grant@kinholdadvisory.com.au</span>
    </li>
  </ul>
</section>

<section class="card card--back" aria-label="Card back">
  <div class="affiliation">
    <div class="affiliation__mark" aria-hidden="true"></div>
    <div class="affiliation__name">Australasian Guild of Trade Brokers</div>
  </div>

  <div class="badge" role="img" aria-label="Advisor member badge"></div>

  <div class="powered">
    <div class="powered__label">Powered by</div>
    <div class="powered__brand">
      <span class="powered__square" aria-hidden="true"></span>
      <span>Oakvale Trade Brokers</span>
    </div>
  </div>

  <div class="legal">
    ABN: 47 291 803 556<br>
    Licensed Real Estate &amp;<br>
    Business Agent No. RA53917<br>
    KTR Adviser Holdings Pty Ltd<br>
    AFSL No. 529361
  </div>
</section>

</body>
</html>
```